Business Cards Needed For Veterinary Business

Looking for a business card design for a veterinary blood bank. We would like it to be clean and professional on appearance but still warm and inviting. We would like to utilize our logo and similar coloring. We will use our phone number, email, website, employee name, employee title.

We do not want a bunch of animated animal photos but do not need the style to be as clinical as a laboratory or human medical procedure office.

We are looking for some creative ideas to choose from so that we can generate a standout professional business card for our management team to utilize.

Target Market(s)

professionals

Industry/Entity Type

veterinary

Contact Information for Business Card

employee name, employee title, phone number, website URL, email

Font styles to use
Sans Serif

Colors
0054AA
0677BA
7BADD7
CADEEF
E8F1F8
EB3D1F
EC4F4E
F09395
F8D3D4
FCEDEE

Requirements
Nice to have
• creative design
Should not have
• animated photos

```html
<!DOCTYPE html>
<html lang="en">
<head>
<meta charset="utf-8">
<title>Northfield Animal Blood Bank – Business Cards</title>
<link href="https://fonts.googleapis.com/css2?family=Montserrat:wght@700;800&family=Roboto:wght@400;500;700&display=swap" rel="stylesheet">
<style>
  :root {
    --stage: #232323;
    --card: #efefef;
    --red: #cf1f2a;
    --blue: #0f4a93;
    --ink: #2b2b2b;
    --muted: #3a3a3a;
    --white: #ffffff;
  }
  * { margin: 0; padding: 0; box-sizing: border-box; }
  html, body { width: 1200px; height: 576px; overflow: hidden; background: var(--stage); }
  .stage { position: relative; width: 1200px; height: 576px; }

  .card {
    position: absolute;
    background: var(--card);
    border-radius: 8px;
    overflow: hidden;
    font-family: "Roboto", Arial, sans-serif;
    color: var(--ink);
  }
  .card--front { left: 102px; top: 139px; width: 484px; height: 292px; }
  .card--back  { left: 596px; top: 138px; width: 480px; height: 291px; }

  /* Brand lockup: plain circle + name */
  .brand { position: absolute; display: flex; align-items: center; }
  .brand__dot { border-radius: 50%; background: var(--red); flex: none; }
  .brand__name {
    font-family: "Montserrat", Arial, sans-serif;
    font-weight: 800;
    color: var(--red);
    text-transform: uppercase;
    line-height: 1.05;
    white-space: nowrap;
  }
  .card--front .brand { left: 80px; top: 62px; gap: 16px; }
  .card--front .brand__dot { width: 78px; height: 78px; }
  .card--front .brand__name { font-size: 27px; }
  .card--back .brand { left: 36px; top: 94px; gap: 11px; max-width: 220px; }
  .card--back .brand__dot { width: 56px; height: 56px; }
  .card--back .brand__name { font-size: 18px; }

  /* Front footer */
  .front__web {
    position: absolute; left: 0; right: 0; top: 236px;
    display: flex; justify-content: center; align-items: center; gap: 10px;
    font-size: 13px; color: var(--muted);
  }
  .front__web .accent { color: var(--red); }
  .front__rule { width: 54px; height: 2px; background: var(--red); }
  .front__band { position: absolute; left: 0; bottom: 0; width: 484px; height: 18px; }

  /* Back details */
  .person { position: absolute; left: 282px; top: 56px; }
  .person__name { font-size: 18px; font-weight: 700; color: var(--red); }
  .person__title { font-size: 12.5px; margin-top: 3px; color: var(--muted); }

  .contact { position: absolute; left: 288px; top: 110px; list-style: none; font-size: 12.5px; color: var(--muted); }
  .contact li { display: flex; align-items: center; gap: 8px; height: 18.5px; }
  .contact svg { width: 11px; height: 11px; flex: none; }
  .address { position: absolute; left: 282px; top: 170px; font-size: 12.5px; line-height: 19px; color: var(--muted); }

  .back__band { position: absolute; left: 0; bottom: 0; width: 480px; height: 37px; }
  .back__tag { position: absolute; left: 282px; top: 262px; font-size: 12.5px; color: var(--white); }
</style>
</head>
<body>
<div class="stage">

  <section class="card card--front">
    <div class="brand">
      <span class="brand__dot"></span>
      <span class="brand__name">Northfield<br>Animal<br>Blood Bank</span>
    </div>
    <div class="front__web">
      <span class="front__rule"></span>
      <span>www.nf<span class="accent">blood</span>bank.com</span>
      <span class="front__rule"></span>
    </div>
    <svg class="front__band" viewBox="0 0 484 18" preserveAspectRatio="none">
      <polygon points="0,0 242,0 226,18 0,18" fill="var(--blue)"/>
      <polygon points="248,0 484,0 484,18 232,18" fill="var(--red)"/>
    </svg>
  </section>

  <section class="card card--back">
    <div class="brand">
      <span class="brand__dot"></span>
      <span class="brand__name">Northfield<br>Animal<br>Blood Bank</span>
    </div>

    <div class="person">
      <div class="person__name">John Doe Smith</div>
      <div class="person__title">Managing Director</div>
    </div>

    <ul class="contact">
      <li>
        <svg viewBox="0 0 12 12"><path d="M1 4c0-2 2-3 5-3s5 1 5 3v1H8V4H4v1H1zM3 6h6l1 5H2z" fill="var(--red)"/></svg>
        828-111-1111
      </li>
      <li>
        <svg viewBox="0 0 12 12"><rect x="1" y="2.5" width="10" height="7" fill="var(--red)"/><path d="M1 2.5l5 4 5-4" stroke="var(--card)" fill="none"/></svg>
        john@yourwebsite.com
      </li>
      <li>
        <svg viewBox="0 0 12 12"><circle cx="6" cy="6" r="5" fill="var(--red)"/><path d="M1 6h10M6 1v10M3 3q3 2 6 0M3 9q3-2 6 0" stroke="var(--card)" stroke-width=".7" fill="none"/></svg>
        www.yourwebsite.com
      </li>
    </ul>
    <div class="address">234 Anywhere St., Any City,<br>Any Town, US 123456</div>

    <svg class="back__band" viewBox="0 0 480 37" preserveAspectRatio="none">
      <defs>
        <linearGradient id="thinBand" x1="0" x2="1">
          <stop offset="0" stop-color="var(--red)"/>
          <stop offset="1" stop-color="#3b3f8f"/>
        </linearGradient>
        <linearGradient id="tabBand" x1="0" x2="1">
          <stop offset="0" stop-color="var(--red)"/>
          <stop offset="1" stop-color="var(--blue)"/>
        </linearGradient>
      </defs>
      <rect x="0" y="26" width="480" height="11" fill="url(#thinBand)"/>
      <path d="M228 37 L244 6 Q247 0 254 0 L480 0 L480 37 Z" fill="url(#tabBand)"/>
    </svg>
    <div class="back__tag">NF Animal Blood Bank</div>
  </section>

</div>
</body>
</html>
```